Now Leasing Banner

Looking for a banner that says the following information approx 4' x 30'

Now Leasing Maplewood Terrace 925-318-6054

Target Market(s)

Drive by traffic

Industry/Entity Type

Residential property management

Requirements
Must have
• Clear and readable from a distance

```html
<!DOCTYPE html>
<html lang="en">
<head>
<meta charset="utf-8">
<title>Now Leasing Banner – Maplewood Terrace</title>
<link rel="stylesheet" href="https://fonts.googleapis.com/css2?family=Anton&family=Oswald:wght@500;600&display=swap">
<style>
  :root {
    --yellow: #fff200;
    --charcoal: #333333;
    --black: #222222;
    --navy: #2e3192;
    --cyan: #00aeef;
    --white: #ffffff;
    --bg-light: #f2f2f2;
    --bg-dark: #7f7f7f;
  }
  * { margin: 0; padding: 0; box-sizing: border-box; }
  html, body { width: 1200px; height: 675px; overflow: hidden; }
  body {
    position: relative;
    background: radial-gradient(ellipse 70% 75% at 50% 50%, var(--bg-light) 0%, #c4c4c4 55%, var(--bg-dark) 100%);
  }
  .banner {
    position: absolute;
    left: 134px;
    width: 932px;
    height: 124px;
    display: flex;
    overflow: visible;
    box-shadow: 0 12px 16px -4px rgba(0,0,0,.35);
  }
  .banner--classic { top: 84px; }
  .banner--bold { top: 276px; }
  .banner--night { top: 473px; }

  .banner__tag {
    position: relative;
    flex: 0 0 auto;
    height: 100%;
    display: flex;
    flex-direction: column;
    justify-content: center;
    align-items: center;
    z-index: 1;
  }
  .banner__tag::after {
    content: "";
    position: absolute;
    right: -17px;
    top: 50%;
    width: 17px;
    height: 36px;
    transform: translateY(-50%);
    background: inherit;
    clip-path: polygon(0 0, 100% 50%, 0 100%);
  }
  .banner__name {
    flex: 1 1 0;
    min-width: 0;
    height: 100%;
    display: flex;
    align-items: center;
    justify-content: center;
    white-space: nowrap;
    text-transform: uppercase;
    padding: 0 20px 0 32px;
    overflow: hidden;
  }
  .tag__headline, .tag__phone { line-height: 1.02; white-space: nowrap; }

  /* Classic: charcoal + yellow */
  .banner--classic .banner__tag { width: 312px; background: var(--charcoal); }
  .banner--classic .tag__headline,
  .banner--classic .tag__phone { font-family: "Oswald", sans-serif; font-weight: 500; font-size: 46px; }
  .banner--classic .tag__headline { color: var(--yellow); }
  .banner--classic .tag__phone { color: var(--white); }
  .banner--classic .banner__name {
    background: var(--yellow);
    color: var(--charcoal);
    font-family: "Oswald", sans-serif;
    font-weight: 600;
    font-size: 64px;
    letter-spacing: -0.5px;
  }

  /* Bold: navy + cyan */
  .banner--bold .banner__tag { width: 301px; background: var(--navy); }
  .banner--bold .tag__headline,
  .banner--bold .tag__phone { font-family: "Anton", sans-serif; font-size: 44px; }
  .banner--bold .tag__headline { color: var(--yellow); }
  .banner--bold .tag__phone { color: var(--white); }
  .banner--bold .banner__name {
    background: var(--cyan);
    color: var(--white);
    font-family: "Anton", sans-serif;
    font-size: 70px;
    -webkit-text-stroke: 4px var(--navy);
    paint-order: stroke fill;
    text-shadow: 3px 4px 0 var(--navy);
  }

  /* Night: yellow + black */
  .banner--night .banner__tag { width: 301px; background: var(--yellow); }
  .banner--night .tag__headline,
  .banner--night .tag__phone { font-family: "Anton", sans-serif; font-size: 44px; color: var(--black); }
  .banner--night .banner__name {
    background: var(--black);
    color: var(--cyan);
    font-family: "Anton", sans-serif;
    font-size: 70px;
    -webkit-text-stroke: 3px var(--white);
    paint-order: stroke fill;
  }
</style>
</head>
<body>
  <section class="banner banner--classic">
    <div class="banner__tag">
      <p class="tag__headline">NOW LEASING</p>
      <p class="tag__phone">925-318-6054</p>
    </div>
    <h1 class="banner__name">Maplewood Terrace</h1>
  </section>

  <section class="banner banner--bold">
    <div class="banner__tag">
      <p class="tag__headline">NOW LEASING</p>
      <p class="tag__phone">925-318-6054</p>
    </div>
    <h2 class="banner__name">Maplewood Terrace</h2>
  </section>

  <section class="banner banner--night">
    <div class="banner__tag">
      <p class="tag__headline">Now Leasing</p>
      <p class="tag__phone">925-318-6054</p>
    </div>
    <h2 class="banner__name">Maplewood Terrace</h2>
  </section>
</body>
</html>
```